models required for semi permeanant eyebrow treatment

The flyer design needs to be simple and not too much fuss.
I would like to specify that im completing my training with lorna quill silken arch which is the leading training team in semi permeanant makeup and I require models for hairstroke eyebrow treatment . The charge is £100 and potential clients would require to consultation prior to the treatment
my contact details including my email and telephone number should be included
mabel
07531642098

• Because im already attaching a before and after photo I thinknto add any other sketches would make the flyer to cluttered so just to keep it simple and to the point and neat and structured but at the same time quiete pretty and feminine

```html
<!DOCTYPE html>
<html lang="en">
<head>
<meta charset="utf-8">
<title>Models Required – Semi Permanent Eyebrow Treatment</title>
<link rel="stylesheet" href="https://fonts.googleapis.com/css2?family=Great+Vibes&family=Roboto+Condensed:wght@300;400&family=Arimo:wght@400;700&display=swap">
<style>
  :root {
    --backdrop: #e6e4e6;
    --magenta: #cc005f;
    --plum: #8a1f7c;
    --paper: #ffffff;
    --ink: #2e2e2e;
    --rose: #c8126a;
    --photo-dark: #3b3a33;
    --photo-skin: #b89f8e;
  }
  * { box-sizing: border-box; margin: 0; padding: 0; }
  html, body {
    width: 1200px; height: 1000px; overflow: hidden;
    background: var(--backdrop);
  }
  .flyer {
    position: absolute; left: 123px; top: 162px;
    width: 955px; height: 675px;
    background: var(--magenta);
    overflow: hidden;
  }
  .flyer__shapes { position: absolute; inset: 0; }
  .headline {
    position: absolute; left: 45px; top: 48px;
    font-family: "Great Vibes", cursive;
    font-size: 60px; line-height: 62px;
    color: var(--ink);
    -webkit-text-stroke: 0.6px currentColor;
  }
  .headline__accent { color: var(--rose); display: block; }
  .offer {
    position: absolute; left: 47px; top: 316px; width: 360px;
    font-family: "Roboto Condensed", sans-serif;
    font-weight: 300; font-size: 33px; line-height: 44px;
    color: var(--paper);
  }
  .contact {
    position: absolute; left: 47px; top: 560px;
    font-family: "Arimo", sans-serif; color: var(--plum);
  }
  .contact__label { font-size: 24px; color: var(--ink); font-weight: 400; }
  .contact__name { font-size: 32px; font-weight: 700; }
  .contact__phone { font-size: 33px; font-weight: 700; line-height: 44px; display: block; }
  .result {
    position: absolute; left: 509px; width: 415px;
  }
  .result--before { top: 83px; }
  .result--after { top: 356px; }
  .result__photo {
    height: 210px; border: 7px solid var(--paper); border-radius: 24px;
    background: linear-gradient(90deg, var(--photo-dark) 0%, var(--photo-skin) 22%, #c6ab98 50%, var(--photo-skin) 78%, var(--photo-dark) 100%);
  }
  .result--after .result__photo { height: 207px; }
  .result__label {
    margin-top: 7px; text-align: center;
    font-family: "Arimo", sans-serif; font-size: 21px;
    color: var(--paper); letter-spacing: 0.5px;
  }
</style>
</head>
<body>
  <main class="flyer">
    <svg class="flyer__shapes" width="955" height="675" viewBox="0 0 955 675" aria-hidden="true">
      <path class="shape-plum" fill="#8a1f7c" d="M0,0 H455 C505,90 505,230 460,330 C425,420 415,560 445,675 H0 Z"/>
      <path class="shape-top" fill="#ffffff" d="M0,0 H445 C487,80 492,185 462,247 C380,232 300,262 205,295 C120,322 55,292 0,268 Z"/>
      <path class="shape-bottom" fill="#ffffff" d="M0,532 C80,502 160,490 250,512 C320,530 370,548 396,556 C401,600 406,640 418,675 H0 Z"/>
    </svg>

    <h1 class="headline">
      Models Required<br>For Semi Permanent
      <span class="headline__accent">Eyebrow Treatment</span>
    </h1>

    <p class="offer">The charge is £100 and potential clients would require to consultation prior to the treatment</p>

    <p class="contact">
      <span class="contact__label">Contact:</span> <span class="contact__name">Mabel</span>
      <span class="contact__phone">07531642098</span>
    </p>

    <figure class="result result--before">
      <div class="result__photo" role="img" aria-label="Close-up photo of a client's eyes and eyebrows before treatment"></div>
      <figcaption class="result__label">BEFORE</figcaption>
    </figure>

    <figure class="result result--after">
      <div class="result__photo" role="img" aria-label="Close-up photo of a client's eyes and eyebrows after treatment"></div>
      <figcaption class="result__label">AFTER</figcaption>
    </figure>
  </main>
</body>
</html>
```